Business Card Design

Im a makeup artist looking for some business cards but need help with creating it.

Industry/Entity Type

Business

Contact Information for Business Card

Mara Penhallow
email mara.penhallow3@brindlemail.net
phone number 0284630928

Requirements
Must have
• i have a logo that i think would work and that i have as my logo on Lumigram. i would like maybe something at the bottom on the card saying like me on Lumigram or something like that.
Nice to have
• Nice writing, my logo as the main item. So its what people are drawn too. to have a glossy card.

```html
<!DOCTYPE html>
<html lang="en">
<head>
<meta charset="utf-8">
<title>Mara Penhallow – Business Card</title>
<link rel="stylesheet" href="https://fonts.googleapis.com/css2?family=Tinos&family=Satisfy&display=swap">
<style>
  :root {
    --backdrop: #2a2a2a;
    --card-light: #ffffff;
    --card-dark: #000000;
    --orchid: #bb62a8;
    --ink: #111111;
    --smoke: #b9b9b9;
    --paper-text: #f2f2f2;
  }
  * { margin: 0; padding: 0; box-sizing: border-box; }
  html, body {
    width: 1200px;
    height: 1000px;
    overflow: hidden;
    background: var(--backdrop);
  }
  .card {
    position: absolute;
    left: 120px;
    top: 230px;
    width: 960px;
    height: 540px;
    display: grid;
    grid-template-columns: 470px 490px;
    grid-template-rows: 496px 44px;
    box-shadow: 0 18px 40px rgba(0,0,0,0.55);
  }
  .card__brand {
    position: relative;
    background: var(--card-light);
    display: flex;
    align-items: center;
    justify-content: center;
  }
  .brand__art {
    position: absolute;
    left: 95px;
    top: 70px;
    width: 280px;
    height: 340px;
    border-radius: 50%;
    background: radial-gradient(ellipse at center, rgba(150,150,150,0.55) 0%, rgba(200,200,200,0.3) 45%, rgba(255,255,255,0) 72%);
  }
  .brand__name {
    position: relative;
    font-family: "Tinos", "Times New Roman", serif;
    font-weight: 400;
    font-size: 42px;
    letter-spacing: 1px;
    color: var(--ink);
    text-transform: uppercase;
  }
  .card__details {
    background: var(--card-dark);
    display: flex;
    flex-direction: column;
    align-items: center;
    font-family: "Tinos", "Times New Roman", serif;
    color: var(--paper-text);
  }
  .details__name {
    margin-top: 74px;
    font-size: 40px;
    font-weight: 400;
    letter-spacing: 2px;
    color: var(--orchid);
    text-transform: uppercase;
  }
  .details__contact {
    list-style: none;
    margin-top: 62px;
    font-size: 23px;
    text-align: center;
  }
  .details__contact li {
    display: flex;
    align-items: center;
    justify-content: center;
    gap: 10px;
    margin-bottom: 16px;
  }
  .contact__icon { width: 22px; height: 22px; flex: none; }
  .details__follow {
    margin-top: 30px;
    font-family: "Satisfy", cursive;
    font-size: 34px;
    color: var(--paper-text);
  }
  .follow__arrow { width: 60px; height: 56px; margin-top: 6px; }
  .follow__network {
    margin-top: 8px;
    font-size: 36px;
    color: var(--orchid);
    letter-spacing: 1px;
  }
  .card__band {
    grid-column: 1 / 3;
    background: var(--orchid);
  }
</style>
</head>
<body>
  <div class="card">
    <section class="card__brand">
      <div class="brand__art" role="img" aria-label="Makeup brush with a soft smoke swirl behind the brand name"></div>
      <p class="brand__name">Mara Penhallow</p>
    </section>

    <section class="card__details">
      <h1 class="details__name">Mara Penhallow</h1>
      <ul class="details__contact">
        <li>
          <svg class="contact__icon" viewBox="0 0 24 24" aria-hidden="true">
            <path fill="var(--orchid)" d="M6.6 10.8a15.1 15.1 0 0 0 6.6 6.6l2.2-2.2c.3-.3.7-.4 1-.2 1.1.4 2.3.6 3.6.6.6 0 1 .4 1 1V20c0 .6-.4 1-1 1A17 17 0 0 1 3 4c0-.6.4-1 1-1h3.5c.6 0 1 .4 1 1 0 1.3.2 2.5.6 3.6.1.3 0 .7-.2 1z"/>
          </svg>
          <span>0284630928</span>
        </li>
        <li>
          <svg class="contact__icon" viewBox="0 0 24 24" aria-hidden="true">
            <rect x="2" y="5" width="20" height="14" fill="var(--orchid)"/>
            <path d="M2 5l10 8 10-8" fill="none" stroke="var(--card-dark)" stroke-width="1.6"/>
          </svg>
          <span>mara.penhallow3@brindlemail.net</span>
        </li>
      </ul>
      <p class="details__follow">Like me on</p>
      <svg class="follow__arrow" viewBox="0 0 60 56" aria-hidden="true">
        <path d="M8 14 C 22 2, 44 4, 42 30" fill="none" stroke="var(--orchid)" stroke-width="8" stroke-linecap="round"/>
        <path d="M28 28 L42 50 L54 26 Z" fill="var(--orchid)"/>
      </svg>
      <p class="follow__network">Lumigram</p>
    </section>

    <div class="card__band"></div>
  </div>
</body>
</html>
```